Business Cards/Stationary for New Travel Agency
Bright Compass Travel
Business Cards/Stationary for New Travel Agency - Travel
Creative Brief
Professional
Melvor Tansley
Leisure and Business Travel Agent
OakVale Court Office, 418 Brindle Blvd., 4th Floor, Santa Monica, CA, 90408 Tel: 310-555-0193 Go Yonder Office, 526 Fenwick Ave., #C, Santa Monica, CA, 90406 Tel: 310-555-0147 ext. 3871
melvor@brightcompasstravelagency.example
www.brightcompasstravelagency.example
Go Yonder Affiliate - CST# 2937516-82
Contact information for both addresses needed on front of business cards. (Two separate columns with each address may look better.) Font size should be big as possible without looking too crowded. Affiliate/License No. can be in small print on bottom of business cards.
Logo on white background. (Big)
drumreed drumreed
loverdan loverdan
#80 - On the back, can you please change Go Yonder Affiliate to Cobble Tours Affiliate and make the font size bigger? Can you please make the font size bigger for the front of the card? (When I adjust the card on the screen to actual size, the font size is too small which will make it difficult for older people to read.)
To all designers: Please upload business card design in mock-up/printer-ready format to see actual size and text. Thank you!!

```html
<!DOCTYPE html>
<html lang="en">
<head>
<meta charset="utf-8">
<title>Bright Compass Travel – Business Card</title>
<link rel="stylesheet" href="https://fonts.googleapis.com/css2?family=Tinos:wght@400;700&display=swap">
<style>
  :root {
    --navy: #1b3b6b;
    --navy-deep: #173560;
    --green: #2e8b3a;
    --blue: #1f5fa8;
    --gold: #f2b51c;
    --ink: #333a44;
    --paper: #ffffff;
    --faint: rgba(255,255,255,0.08);
  }
  html, body {
    margin: 0;
    padding: 0;
    width: 1200px;
    height: 418px;
    overflow: hidden;
    background: var(--paper);
    font-family: "Tinos", "Times New Roman", serif;
  }
  .canvas { position: relative; width: 1200px; height: 418px; }

  .card { position: absolute; top: 14px; width: 576px; height: 399px; overflow: hidden; }
  .card-front { left: 10px; background: var(--paper); box-shadow: 0 0 3px rgba(0,0,0,0.25); }
  .card-back { left: 614px; top: 10px; height: 403px; background: var(--navy); }

  .agent-name { position: absolute; left: 26px; top: 20px; margin: 0; font-size: 23px; font-weight: 400; color: var(--navy); }
  .agent-role { position: absolute; left: 26px; top: 52px; font-size: 14px; color: var(--green); }
  .agent-mobile { position: absolute; left: 26px; top: 78px; font-size: 15px; color: var(--ink); display: flex; align-items: center; gap: 8px; }

  .brand-front { position: absolute; left: 370px; top: 60px; width: 190px; display: flex; align-items: center; gap: 10px; }
  .brand-dot { width: 22px; height: 22px; border-radius: 50%; background: var(--gold); flex: none; }
  .brand-name { font-size: 22px; line-height: 1.1; color: var(--green); }

  .office { position: absolute; top: 180px; font-size: 12.5px; line-height: 19px; color: var(--ink); }
  .office-one { left: 26px; }
  .office-two { left: 250px; }
  .office-title { color: var(--green); font-weight: 700; }

  .contact-list { position: absolute; top: 300px; font-size: 13.5px; line-height: 24px; color: var(--ink); }
  .contact-phones { left: 26px; }
  .contact-online { left: 250px; }
  .contact-line { display: flex; align-items: center; gap: 8px; }
  .web { color: var(--green); font-size: 15px; }

  .stripe { position: absolute; bottom: 0; height: 14px; }
  .stripe-gold { left: 0; width: 200px; background: var(--gold); }
  .stripe-blue { left: 200px; width: 196px; background: var(--blue); }
  .stripe-green { left: 396px; width: 180px; background: var(--green); }

  .back-mark { position: absolute; left: 30px; top: 80px; width: 260px; height: 260px; border-radius: 50%; background: var(--faint); }
  .brand-back { position: absolute; left: 240px; top: 160px; width: 320px; text-align: center; color: #fff; }
  .brand-back-name { font-size: 29px; letter-spacing: 1px; }
  .affiliate { position: absolute; left: 360px; top: 340px; font-size: 12px; line-height: 16px; color: var(--gold); }
</style>
</head>
<body>
<div class="canvas">

  <section class="card card-front">
    <h1 class="agent-name">Melvor Tansley</h1>
    <div class="agent-role">Leisure And Business Travel Agent</div>
    <div class="agent-mobile">
      <svg width="12" height="16" viewBox="0 0 12 16" aria-hidden="true"><rect x="1" y="0.5" width="10" height="15" rx="2" fill="var(--gold)"/><rect x="3" y="2.5" width="6" height="9" fill="#fff"/></svg>
      310-555-0128
    </div>

    <div class="brand-front">
      <span class="brand-dot"></span>
      <span class="brand-name">Bright Compass Travel</span>
    </div>

    <div class="office office-one">
      <div class="office-title">OakVale Court Office</div>
      <div>418 Brindle Blvd., 4th Floor</div>
      <div>Santa Monica, CA, 90408</div>
      <div>Tel: 310-555-0193</div>
    </div>
    <div class="office office-two">
      <div class="office-title">Go Yonder Office</div>
      <div>526 Fenwick Ave., #C</div>
      <div>Santa Monica, CA, 90406</div>
      <div>Tel: 310-555-0147 Ext. 3871</div>
    </div>

    <div class="contact-list contact-phones">
      <div class="contact-line">
        <svg width="16" height="14" viewBox="0 0 16 14" aria-hidden="true"><path d="M2 4 Q8 0 14 4 L12 6 L10 4.5 L6 4.5 L4 6 Z" fill="var(--gold)"/><rect x="3" y="7" width="10" height="6" rx="1" fill="var(--gold)"/></svg>
        800-555-0162
      </div>
      <div class="contact-line">
        <svg width="16" height="14" viewBox="0 0 16 14" aria-hidden="true"><rect x="1" y="4" width="14" height="9" rx="1" fill="var(--green)"/><rect x="4" y="1" width="8" height="4" fill="var(--green)"/></svg>
        310-555-0174
      </div>
    </div>
    <div class="contact-list contact-online">
      <div class="contact-line">
        <svg width="16" height="12" viewBox="0 0 16 12" aria-hidden="true"><rect x="0.5" y="0.5" width="15" height="11" fill="var(--gold)"/><path d="M0.5 0.5 L8 7 L15.5 0.5" fill="none" stroke="#fff" stroke-width="1.2"/></svg>
        melvor@brightcompasstravelagency.example
      </div>
      <div class="contact-line web">www.brightcompasstravelagency.example</div>
    </div>

    <div class="stripe stripe-gold"></div>
    <div class="stripe stripe-blue"></div>
    <div class="stripe stripe-green"></div>
  </section>

  <section class="card card-back">
    <div class="back-mark"></div>
    <div class="brand-back">
      <div class="brand-back-name">Bright Compass Travel</div>
    </div>
    <div class="affiliate">
      <div>Go Yonder Affiliate</div>
      <div>CST# 2937516-82</div>
    </div>
  </section>

</div>
</body>
</html>
```